Fenrui Tea Factory ripe puerh mini tea cakes package *

We need soft packaging for loose tea for Zarbelo USA market, based on design we liked. You can find it on attached files. Tea cup (kettle, mug, etc) with strong black tea in it.
A popular diet tea for daily use. It is also a perfect travel tea, suitable for people who lead an active lifestyle. Contains caffeine, vitamins and minerals. It invigorates, warms and raises the mood.
Messages for project: health, invigorating, activity, slimming, detox

Target Market(s)

Zarbelo USA market

Industry/Entity Type

Factory

Colors

Designer to choose colors to be used in the design.

Requirements
Must have
• Puerh mini tea cakes, Fenrui tea factory logo TM (red colour) on the top of frontier, 100% Natural Menghai ripe puerh tea, L-theanine for good mood, Caffeine for boost energy, 20 pcs + 25%, Premium Quality, individual package for every tea cake (nearly 5 gramm)
Nice to have
• Newspaper style, healthy, energy, vitamine, active style life. Aroma, taste, colour diagrams, tea leaves, tea cup or mug, any other image symbollizing good teadrinking.
• Suitable for all brewing methods, Old Yunnan Tea garden
Should not have
• product images itself (mini tea cakes)

```html
<!DOCTYPE html>
<html lang="en">
<head>
<meta charset="utf-8">
<title>Fenrui Puerh Mini Tea Cakes – Pack Front</title>
<link href="https://fonts.googleapis.com/css2?family=Alfa+Slab+One&family=Abril+Fatface&family=Oswald:wght@400;500;600&family=Playfair+Display:ital,wght@0,400;0,700;1,400&display=swap" rel="stylesheet">
<style>
  :root {
    --stage: #e4e4e4;
    --paper: #f0efe9;
    --ink: #1c1a17;
    --gold: #8b6f3f;
    --title-shadow: #3fa34a;
    --label: #4a8a57;
    --red: #e3141b;
    --white: #ffffff;
  }
  * { margin: 0; padding: 0; box-sizing: border-box; }
  html, body { width: 1200px; height: 1055px; overflow: hidden; background: var(--stage); }
  .pack-front {
    position: absolute; left: 289px; top: 3px;
    width: 631px; height: 1065px;
    background: var(--paper);
    transform: scale(0.985); transform-origin: top left;
    box-shadow: 0 6px 18px rgba(0,0,0,.15);
    font-family: "Playfair Display", Georgia, serif;
    color: var(--ink);
    overflow: hidden;
  }
  .abs { position: absolute; }
  .kicker { font-size: 9px; letter-spacing: .5px; top: 32px; text-transform: uppercase; }
  .kicker--left { left: 14px; }
  .kicker--right { right: 22px; }
  .double-rule { height: 7px; border-top: 3px solid var(--ink); border-bottom: 1px solid var(--ink); }
  .brand-block {
    left: 245px; top: 0; width: 141px; height: 92px; background: var(--red);
    display: flex; align-items: flex-end; justify-content: center; padding-bottom: 10px;
  }
  .brand-name { font-family: "Oswald", sans-serif; font-weight: 500; font-size: 18px; color: var(--white); letter-spacing: .5px; }
  .headline {
    left: 0; width: 631px; text-align: center; white-space: nowrap;
    font-family: "Alfa Slab One", serif; color: var(--gold);
    font-size: 92px; line-height: 1;
    text-shadow: 3px 3px 0 var(--title-shadow);
  }
  .headline span { display: inline-block; transform-origin: center; }
  .headline--one { top: 102px; }
  .headline--one span { transform: scaleX(.86); }
  .headline--two { top: 207px; }
  .headline--two span { transform: scaleX(.95); }
  .rule { height: 0; border-top: 2px solid var(--ink); }
  .tagline {
    left: 14px; width: 598px; top: 326px; text-align: justify; text-align-last: justify;
    font-family: "Oswald", sans-serif; font-size: 20px; letter-spacing: 6px; white-space: nowrap;
  }
  .hero-photo { left: 14px; top: 370px; width: 598px; height: 402px; }
  .mood-label {
    left: 25px; top: 380px; width: 193px; height: 80px; background: var(--label);
    color: var(--white); font-family: "Oswald", sans-serif; padding: 8px 10px; line-height: 1;
  }
  .mood-label span { display: block; font-size: 25px; }
  .mood-label span + span { font-size: 34px; margin-top: 2px; }
  .cup-photo { left: 360px; top: 720px; width: 270px; height: 165px; }
  .energy-box {
    left: 14px; top: 827px; width: 151px; height: 156px; background: var(--ink);
    text-align: center; padding-top: 14px; line-height: 1;
  }
  .energy-box .small { font-family: "Abril Fatface", serif; color: var(--gold); font-size: 22px; }
  .energy-box .big { font-family: "Abril Fatface", serif; color: var(--gold); font-size: 44px; }
  .energy-box .boost { font-family: "Oswald", sans-serif; font-weight: 500; color: var(--white); font-size: 32px; line-height: 1; }
  .quality {
    left: 176px; top: 833px; font-family: "Abril Fatface", serif; color: var(--gold);
    font-size: 31px; line-height: .9;
  }
  .benefits { left: 176px; top: 895px; font-size: 14.5px; font-weight: 700; white-space: nowrap; }
  .count {
    left: 176px; top: 920px; font-size: 33px; color: var(--gold); white-space: nowrap;
    font-variant-numeric: lining-nums; line-height: 1;
  }
  .count-note { left: 413px; top: 923px; width: 112px; font-size: 8.5px; font-style: italic; line-height: 1.1; }
  .claims {
    left: 534px; top: 920px; border-left: 1px solid var(--ink); padding-left: 5px;
    color: var(--gold); font-weight: 700; line-height: 1; text-transform: uppercase;
  }
  .claims span { display: block; font-size: 16px; }
  .claims span:nth-child(2) { font-size: 12px; }
  .claims span:nth-child(3) { font-size: 8px; }
  .travel { left: 176px; top: 962px; font-family: "Oswald", sans-serif; font-size: 9.5px; white-space: nowrap; }
  .band { left: 14px; top: 985px; width: 596px; height: 20px; display: flex; align-items: center; gap: 8px; }
  .band .bar { flex: 1; height: 16px; background: var(--gold); }
  .band .bar--short { flex: 0 0 155px; }
  .band .text { font-weight: 700; font-size: 17px; color: var(--gold); white-space: nowrap; }
  .footer {
    left: 14px; top: 1023px; width: 596px; display: flex; justify-content: space-between; align-items: baseline;
    font-size: 17px;
  }
  .footer small { font-size: 7px; letter-spacing: .3px; }
  .footer .url { font-size: 12px; }
  .footer .sep { width: 2px; height: 14px; background: var(--ink); }
</style>
</head>
<body>
<main class="pack-front">
  <div class="abs kicker kicker--left">New Energy News</div>
  <div class="abs kicker kicker--right">Fenrui Presents</div>
  <div class="abs double-rule" style="left:14px; top:48px; width:226px;"></div>
  <div class="abs double-rule" style="left:393px; top:48px; width:217px;"></div>
  <div class="abs brand-block"><span class="brand-name">Fenrui Teas</span></div>

  <h1 class="abs headline headline--one"><span>PUERH MINI</span></h1>
  <div class="abs headline headline--two"><span>TEA CAKES</span></div>

  <div class="abs rule" style="left:14px; top:307px; width:596px;"></div>
  <div class="abs tagline">100% NATURAL MENGHAI RIPE PUERH TEA</div>
  <div class="abs rule" style="left:14px; top:361px; width:596px; border-top-width:1px;"></div>

  <svg class="abs hero-photo" role="img" aria-label="Photo of foil-wrapped puerh mini tea cakes in a white bowl" viewBox="0 0 598 402">
    <defs>
      <radialGradient id="bowl" cx="50%" cy="50%" r="60%">
        <stop offset="0" stop-color="#9a8676"/>
        <stop offset=".6" stop-color="#b3a7a3"/>
        <stop offset="1" stop-color="#cfd0d4"/>
      </radialGradient>
    </defs>
    <rect width="598" height="402" fill="url(#bowl)"/>
  </svg>
  <div class="abs mood-label"><span>L-THEANINE FOR</span><span>GOOD MOOD</span></div>

  <svg class="abs cup-photo" role="img" aria-label="Photo of a white cup of amber tea with mint leaves" viewBox="0 0 270 165">
    <defs>
      <radialGradient id="cup" cx="45%" cy="40%" r="55%">
        <stop offset="0" stop-color="#d99a3a"/>
        <stop offset=".45" stop-color="#f3efe8"/>
        <stop offset="1" stop-color="#f3efe8" stop-opacity="0"/>
      </radialGradient>
    </defs>
    <ellipse cx="125" cy="80" rx="125" ry="80" fill="url(#cup)"/>
    <ellipse cx="235" cy="95" rx="32" ry="28" fill="#3f8a3a" opacity=".8"/>
  </svg>

  <div class="abs energy-box">
    <div class="small">Caffeine</div>
    <div class="big">FOR</div>
    <div class="boost">BOOST<br>ENERGY</div>
  </div>

  <div class="abs rule" style="left:176px; top:829px; width:194px; border-top-width:1px;"></div>
  <div class="abs quality">Premium<br>Quality</div>
  <div class="abs benefits">Healthy, energy, vitamine, active style life. Aroma, taste</div>
  <div class="abs rule" style="left:176px; top:917px; width:434px; border-top-width:1px;"></div>
  <div class="abs count">20 PCS + 25%</div>
  <div class="abs count-note">Contains caffeine, vitamins and minerals. It invigorates, warms and raises the mood.</div>
  <div class="abs claims"><span>Detox</span><span>Slimming</span><span>Invigorating</span></div>
  <div class="abs travel">IT IS ALSO A PERFECT TRAVEL TEA, SUITABLE FOR PEOPLE WHO LEAD AN ACTIVE LIFESTYLE.</div>

  <div class="abs band">
    <span class="bar bar--short"></span>
    <span class="text">A popular diet tea for daily use.</span>
    <span class="bar"></span>
  </div>

  <div class="abs double-rule" style="left:14px; top:1012px; width:596px; height:6px; border-top-width:2px;"></div>
  <div class="abs footer">
    <span><small>FRIENDPAGE/</small>FENRUI</span>
    <span class="sep"></span>
    <span class="url">WWW.WEBSITE.COM</span>
    <span class="sep"></span>
    <span><small>CHIRPLINE/</small>FENRUI</span>
  </div>
</main>
</body>
</html>
```